Harbor Lantern Security Solutions Business Cards

We are looking for a "catchy" business card that contains blue and red as well as incorporating our logo design. Gold is also an option. Anything that stands out and looks awesome!!! The final design should communicate security and trust.
We are advertising home security systems with monitoring services, video surveillance as well as custom gates with key pad entry.

Website address: www.bluecrestwardtx.example
Phone number: 936-555-0193
Owner: Marcus Orlend
Located in Larkmoor, Westvale
License Number: K47315
Licensed and Insured
Logo: We're There When You're Not

I'm not sure if all of this is needed, but just in case!!!

Target Market(s)

Commercial and Residential

Industry/Entity Type

Business

Contact Information for Business Card

Owner: Marcus Orlend
Email Address: morlend@mailbeam.example

Font styles to use
Sans Serif

Colors
ec1f27
fbed22
0355a3

Requirements
Must have
• Residential and Commercial Alarm Systems, Monitoring Services. Video Surveillance, Custom Gates and Key Pad Entry
Nice to have
• Everything would be nice although I don't want the card to look overcrowded.

```html
<!DOCTYPE html>
<html lang="en">
<head>
<meta charset="utf-8">
<title>Harbor Lantern Security Solutions – Business Cards</title>
<link rel="stylesheet" href="https://fonts.googleapis.com/css2?family=Arimo:wght@400;700&family=Roboto+Condensed:wght@400&display=swap">
<style>
  :root {
    --page: #ffffff;
    --card-dark: #1c1716;
    --card-light: #ffffff;
    --card-border: #8a8a8a;
    --brand-red: #e0312b;
    --ink: #1f1d1d;
    --rule: #a9a9a9;
    --on-dark: #ffffff;
  }
  * { margin: 0; padding: 0; box-sizing: border-box; }
  html, body { width: 1200px; height: 1200px; overflow: hidden; background: var(--page); }
  body { position: relative; font-family: "Arimo", Arial, sans-serif; color: var(--ink); }

  .card { position: absolute; left: 180px; width: 838px; height: 480px; border-radius: 34px; }
  .card--front { top: 100px; background: var(--card-dark); }
  .card--back { top: 618px; background: var(--card-light); border: 1px solid var(--card-border); }

  .brand { position: absolute; display: flex; flex-direction: column; align-items: center; text-align: center; }
  .brand__dot { border-radius: 50%; background: var(--brand-red); }
  .brand__name { font-weight: 700; text-transform: uppercase; letter-spacing: 1px; line-height: 1.2; }

  .card--front .brand { left: 0; right: 0; top: 84px; }
  .card--front .brand__dot { width: 190px; height: 190px; }
  .card--front .brand__name { color: var(--on-dark); font-size: 22px; margin-top: 20px; }

  .services { position: absolute; left: 0; right: 0; top: 384px; text-align: center;
    font-family: "Roboto Condensed", "Arial Narrow", sans-serif; font-size: 23.5px;
    color: var(--on-dark); line-height: 28px; }

  .card--back .brand { left: 40px; width: 320px; top: 128px; }
  .card--back .brand__dot { width: 160px; height: 160px; }
  .card--back .brand__name { color: var(--ink); font-size: 18px; margin-top: 18px; }

  .divider { position: absolute; left: 364px; top: 72px; width: 2px; height: 336px; background: var(--rule); }

  .contact { position: absolute; left: 402px; top: 98px; }
  .contact__name { font-size: 32px; font-weight: 700; line-height: 36px; }
  .contact__role { font-size: 22px; color: var(--brand-red); line-height: 26px; margin-top: 2px; }
  .contact__list { list-style: none; margin-top: 14px; }
  .contact__item { display: flex; align-items: center; height: 32.5px; font-size: 24px; white-space: nowrap; }
  .contact__icon { width: 30px; margin-left: 2px; margin-right: 10px; display: flex; justify-content: center; }
  .contact__city { font-size: 23px; margin-top: 12px; }
  .contact__license { font-size: 22px; line-height: 28px; margin-top: 12px; }
</style>
</head>
<body>

<section class="card card--front">
  <div class="brand">
    <div class="brand__dot"></div>
    <div class="brand__name">Harbor Lantern<br>Security Solutions</div>
  </div>
  <p class="services">
    Residential and Commercial Alarm Systems<br>
    Monitoring Services | Video Surveillance, Custom Gates and Key Pad Entry
  </p>
</section>

<section class="card card--back">
  <div class="brand">
    <div class="brand__dot"></div>
    <div class="brand__name">Harbor Lantern<br>Security Solutions</div>
  </div>

  <div class="divider"></div>

  <div class="contact">
    <h1 class="contact__name">Marcus Orlend</h1>
    <p class="contact__role">Owner</p>
    <ul class="contact__list">
      <li class="contact__item">
        <span class="contact__icon">
          <svg width="16" height="26" viewBox="0 0 16 26"><rect x="1.5" y="1.5" width="13" height="23" rx="3" fill="none" stroke="#e0312b" stroke-width="2.5"/><circle cx="8" cy="20" r="1.6" fill="#e0312b"/></svg>
        </span>936-555-0193
      </li>
      <li class="contact__item">
        <span class="contact__icon">
          <svg width="26" height="18" viewBox="0 0 26 18"><rect x="0" y="0" width="26" height="18" rx="2" fill="#e0312b"/><path d="M1 1 L13 10 L25 1 M1 17 L10 8 M25 17 L16 8" stroke="#fff" stroke-width="1.6" fill="none"/></svg>
        </span>morlend@mailbeam.example
      </li>
      <li class="contact__item">
        <span class="contact__icon">
          <svg width="22" height="22" viewBox="0 0 22 22"><g fill="none" stroke="#e0312b" stroke-width="2"><circle cx="11" cy="11" r="9.5"/><ellipse cx="11" cy="11" rx="4.5" ry="9.5"/><path d="M1.5 11 H20.5 M3 6 H19 M3 16 H19"/></g></svg>
        </span>www.bluecrestwardtx.example
      </li>
    </ul>
    <p class="contact__city">Larkmoor, Westvale</p>
    <p class="contact__license">License Number: K47315<br>Licensed and Insured</p>
  </div>
</section>

</body>
</html>
```